Powerpoint template for technical & business level presentations

Looking for a powerpoint template to use for professional business & technical presentations that will work well with the logo you designed for us.

Industry/Entity Type

Business

```html
<!DOCTYPE html>
<html lang="en">
<head>
<meta charset="utf-8">
<title>Sample Design_V1</title>
<link rel="stylesheet" href="https://fonts.googleapis.com/css2?family=Arimo:wght@400;700&family=Carlito&display=swap">
<style>
  :root {
    --canvas: #d9d9d9;
    --slide: #ffffff;
    --heading-blue: #2160a8;
    --brand-blue: #1f63b5;
    --lime: #9dc63b;
    --lime-light: #c3dc72;
    --lime-pale: #e4efc4;
    --teal: #3bafc2;
    --teal-dark: #1a8f7c;
    --violet: #5f6fc6;
    --pie-blue: #1a75c4;
    --ink: #222222;
    --muted: #8a8a8a;
    --row-dark: #d9d9d9;
    --row-light: #efefef;
    --axis: #bdbdbd;
  }
  * { box-sizing: border-box; margin: 0; padding: 0; }
  html, body { width: 1200px; height: 900px; overflow: hidden; background: var(--canvas); }
  body { position: relative; font-family: "Arimo", Arial, sans-serif; color: var(--ink); }

  .sheet-title {
    position: absolute; top: 26px; left: 0; width: 1200px; text-align: center;
    font-family: "Carlito", Calibri, sans-serif; font-size: 28px; font-weight: 400; color: var(--heading-blue);
  }

  .slide { position: absolute; width: 341px; height: 255px; background: var(--slide); overflow: hidden; }
  .col-1 { left: 31px; } .col-2 { left: 429px; } .col-3 { left: 827px; }
  .row-1 { top: 84px; } .row-2 { top: 358px; } .row-3 { top: 630px; }

  .artwork-band {
    position: absolute; left: 0; top: 0;
    background: linear-gradient(160deg, var(--lime) 0%, var(--lime-light) 60%, var(--lime-pale) 100%);
  }
  .artwork-corner {
    position: absolute; left: 0; top: 0; width: 30px; height: 16px;
    background: linear-gradient(135deg, var(--lime) 0%, var(--lime-light) 100%);
  }

  .brand {
    position: absolute; display: flex; align-items: center; gap: 6px;
    font-weight: 700; color: var(--brand-blue); letter-spacing: 0.5px; line-height: 1;
  }
  .brand-large { font-size: 18px; }
  .brand-dot { width: 8px; height: 8px; border-radius: 50%; background: var(--lime); }
  .brand-footer { right: 7px; bottom: 8px; font-size: 7px; }

  .cover-title { position: absolute; font-size: 16px; color: var(--lime); }
  .cover-date { position: absolute; font-size: 6px; color: var(--muted); }

  .slide-heading { position: absolute; left: 21px; top: 35px; font-size: 13px; font-weight: 400; line-height: 1.25; color: var(--ink); }
  .bullets { position: absolute; font-size: 8px; line-height: 12px; list-style: none; color: var(--ink); }
  .bullets li { white-space: nowrap; }
  .lvl-1::before { content: "•  "; }
  .lvl-2 { padding-left: 17px; } .lvl-2::before { content: "–  "; }
  .lvl-3 { padding-left: 34px; } .lvl-3::before { content: "•  "; font-size: 6px; }
  .lvl-4 { padding-left: 51px; } .lvl-4::before { content: "–  "; }
  .lvl-5 { padding-left: 68px; } .lvl-5::before { content: "•  "; font-size: 6px; }

  .chart { position: absolute; left: 0; top: 0; font-family: "Arimo", Arial, sans-serif; }
  .chart text { fill: var(--ink); }

  .data-table { position: absolute; left: 18px; top: 58px; width: 304px; border-collapse: collapse; font-size: 5.5px; }
  .data-table th { background: var(--lime); color: var(--ink); font-weight: 400; height: 15px; border-right: 1px solid #ffffff; }
  .data-table th:first-child { text-align: left; padding-left: 4px; }
  .data-table td { height: 15px; text-align: center; border-right: 1px solid #ffffff; border-top: 1px solid #ffffff; }
  .data-table td:first-child { text-align: left; padding-left: 4px; }
  .data-table tr:nth-child(odd) td { background: var(--row-dark); }
  .data-table tr:nth-child(even) td { background: var(--row-light); }
</style>
</head>
<body>
  <h1 class="sheet-title">Sample Design_V1</h1>

  <section class="slide col-1 row-1">
    <div class="artwork-band" style="width:341px;height:106px" role="img" aria-label="Decorative green artwork area"></div>
    <div class="brand brand-large" style="left:24px;top:120px"><span class="brand-dot"></span>LUMENVALE</div>
    <p class="cover-title" style="left:137px;top:181px">Presentation Template</p>
    <p class="cover-date" style="right:34px;top:208px">November 3, 2013</p>
  </section>

  <section class="slide col-2 row-1">
    <div class="artwork-band" style="width:341px;height:90px" role="img" aria-label="Decorative green artwork area"></div>
    <div class="brand brand-large" style="left:226px;top:102px;font-size:14px"><span class="brand-dot"></span>LUMENVALE</div>
    <p class="cover-title" style="left:28px;top:162px;font-size:13px">Divider</p>
  </section>

  <section class="slide col-3 row-1">
    <div class="artwork-corner" role="img" aria-label="Small decorative green accent"></div>
    <h2 class="slide-heading">Title and Bulleted Content</h2>
    <ul class="bullets" style="left:25px;top:61px">
      <li class="lvl-1">Click to edit Master text styles</li>
      <li class="lvl-2">Second level</li>
      <li class="lvl-3">Third level</li>
      <li class="lvl-4">Fourth level</li>
      <li class="lvl-5">Fifth level</li>
    </ul>
    <div class="brand brand-footer">LUMENVALE</div>
  </section>

  <section class="slide col-1 row-2">
    <h2 class="slide-heading" style="left:182px;top:25px;width:155px">Title and Bulleted Content on the Right</h2>
    <ul class="bullets" style="left:182px;top:61px">
      <li class="lvl-1">Click to edit Master text styles</li>
      <li class="lvl-2">Second level</li>
      <li class="lvl-3">Third level</li>
      <li class="lvl-4">Fourth level</li>
      <li class="lvl-5">Fifth level</li>
    </ul>
    <div class="brand brand-footer">LUMENVALE</div>
  </section>

  <section class="slide col-2 row-2">
    <div class="artwork-corner" role="img" aria-label="Small decorative green accent"></div>
    <h2 class="slide-heading">Pie Chart</h2>
    <svg class="chart" width="341" height="255" viewBox="0 0 341 255">
      <text x="169" y="76" font-size="10" text-anchor="middle">Chart Title</text>
      <path d="M169,154 L169,99 A55,55 0 1 1 142.5,202.2 Z" fill="var(--pie-blue)"/>
      <path d="M169,154 L142.5,202.2 A55,55 0 0 1 117.9,133.8 Z" fill="var(--teal)"/>
      <path d="M169,154 L117.9,133.8 A55,55 0 0 1 139.5,107.6 Z" fill="var(--teal-dark)"/>
      <path d="M169,154 L139.5,107.6 A55,55 0 0 1 169,99 Z" fill="var(--lime)"/>
      <g font-size="6.5">
        <text x="226" y="168">1st Qtr</text><text x="230" y="176">58%</text>
        <text x="92" y="170">2nd Qtr</text><text x="97" y="178">23%</text>
        <text x="104" y="108">3rd Qtr</text><text x="108" y="116">10%</text>
        <text x="144" y="91">4th Qtr</text><text x="150" y="99">9%</text>
      </g>
    </svg>
    <div class="brand brand-footer">LUMENVALE</div>
  </section>

  <section class="slide col-3 row-2">
    <div class="artwork-corner" role="img" aria-label="Small decorative green accent"></div>
    <h2 class="slide-heading">Bar Chart</h2>
    <svg class="chart" width="341" height="255" viewBox="0 0 341 255">
      <g stroke="var(--axis)" stroke-width="0.7">
        <line x1="68" y1="79" x2="68" y2="188"/>
        <line x1="68" y1="188" x2="256" y2="188"/>
      </g>
      <g font-size="5" text-anchor="end">
        <text x="64" y="190">0</text><text x="64" y="174">1</text><text x="64" y="159">2</text>
        <text x="64" y="143">3</text><text x="64" y="128">4</text><text x="64" y="112">5</text>
        <text x="64" y="96">6</text><text x="64" y="81">7</text>
      </g>
      <g font-size="5.5" text-anchor="middle">
        <text x="92" y="198">A</text><text x="138" y="198">B</text><text x="184" y="198">C</text><text x="230" y="198">D</text>
      </g>
      <g>
        <rect x="76" y="120.9" width="7" height="67.1" fill="var(--lime)"/>
        <rect x="84" y="150.6" width="7" height="37.4" fill="var(--teal)"/>
        <rect x="92" y="156.8" width="7" height="31.2" fill="var(--teal-dark)"/>
        <rect x="100" y="110" width="7" height="78" fill="var(--violet)"/>
        <rect x="122" y="149" width="7" height="39" fill="var(--lime)"/>
        <rect x="130" y="119.4" width="7" height="68.6" fill="var(--teal)"/>
        <rect x="138" y="141.2" width="7" height="46.8" fill="var(--teal-dark)"/>
        <rect x="146" y="128.7" width="7" height="59.3" fill="var(--violet)"/>
        <rect x="168" y="133.4" width="7" height="54.6" fill="var(--lime)"/>
        <rect x="176" y="159.9" width="7" height="28.1" fill="var(--teal)"/>
        <rect x="184" y="94.4" width="7" height="93.6" fill="var(--teal-dark)"/>
        <rect x="192" y="144.3" width="7" height="43.7" fill="var(--violet)"/>
        <rect x="214" y="117.8" width="7" height="70.2" fill="var(--lime)"/>
        <rect x="222" y="144.3" width="7" height="43.7" fill="var(--teal)"/>
        <rect x="230" y="110" width="7" height="78" fill="var(--teal-dark)"/>
        <rect x="238" y="138.1" width="7" height="49.9" fill="var(--violet)"/>
      </g>
      <g font-size="5" text-anchor="middle">
        <text x="79.5" y="118">4.3</text><text x="87.5" y="148">2.4</text><text x="95.5" y="154">2</text><text x="103.5" y="107">5</text>
        <text x="125.5" y="146">2.5</text><text x="133.5" y="117">4.4</text><text x="141.5" y="139">3</text><text x="149.5" y="126">3.8</text>
        <text x="171.5" y="131">3.5</text><text x="179.5" y="157">1.8</text><text x="187.5" y="92">6</text><text x="195.5" y="142">2.8</text>
        <text x="217.5" y="115">4.5</text><text x="225.5" y="142">2.8</text><text x="233.5" y="107">5</text><text x="241.5" y="136">3.2</text>
      </g>
      <g font-size="5">
        <rect x="267" y="120" width="3" height="3" fill="var(--lime)"/><text x="272" y="123">S1</text>
        <rect x="267" y="130" width="3" height="3" fill="var(--teal)"/><text x="272" y="133">S2</text>
        <rect x="267" y="140" width="3" height="3" fill="var(--teal-dark)"/><text x="272" y="143">S3</text>
        <rect x="267" y="150" width="3" height="3" fill="var(--violet)"/><text x="272" y="153">S4</text>
      </g>
    </svg>
    <div class="brand brand-footer">LUMENVALE</div>
  </section>

  <section class="slide col-1 row-3">
    <div class="artwork-corner" role="img" aria-label="Small decorative green accent"></div>
    <h2 class="slide-heading">Line Chart</h2>
    <svg class="chart" width="341" height="255" viewBox="0 0 341 255">
      <g stroke="var(--axis)" stroke-width="0.7">
        <line x1="46" y1="60" x2="46" y2="191"/>
        <line x1="46" y1="191" x2="246" y2="191"/>
      </g>
      <g font-size="5" text-anchor="end">
        <text x="42" y="193">0</text><text x="42" y="180">0.5</text><text x="42" y="167">1</text>
        <text x="42" y="154">1.5</text><text x="42" y="141">2</text><text x="42" y="128">2.5</text>
        <text x="42" y="114">3</text><text x="42" y="101">3.5</text><text x="42" y="88">4</text>
        <text x="42" y="75">4.5</text><text x="42" y="62">5</text>
      </g>
      <g font-size="5" text-anchor="middle">
        <text x="72" y="200">Category 1</text><text x="121" y="200">Category 2</text>
        <text x="171" y="200">Category 3</text><text x="221" y="200">Category 4</text>
      </g>
      <g fill="none" stroke-width="1.1">
        <polyline points="72,78.3 121,125.5 171,99.3 221,73.1" stroke="var(--teal-dark)"/>
        <polyline points="72,128.1 121,75.7 171,143.8 221,117.6" stroke="var(--teal)"/>
        <polyline points="72,164.8 121,159.6 171,122.9 221,151.7" stroke="var(--lime)"/>
        <polyline points="72,180.5 121,101.9 171,73.1 221,94.1" stroke="var(--violet)"/>
      </g>
      <g>
        <rect x="70.5" y="76.8" width="3" height="3" fill="var(--teal-dark)"/>
        <rect x="119.5" y="124" width="3" height="3" fill="var(--teal-dark)"/>
        <rect x="169.5" y="97.8" width="3" height="3" fill="var(--teal-dark)"/>
        <rect x="219.5" y="71.6" width="3" height="3" fill="var(--teal-dark)"/>
        <circle cx="72" cy="180.5" r="1.6" fill="var(--violet)"/>
        <circle cx="121" cy="101.9" r="1.6" fill="var(--violet)"/>
        <circle cx="171" cy="73.1" r="1.6" fill="var(--violet)"/>
        <circle cx="221" cy="94.1" r="1.6" fill="var(--violet)"/>
      </g>
      <g font-size="5" text-anchor="middle">
        <text x="72" y="74">4.3</text><text x="121" y="71">4.4</text><text x="171" y="95">3.5</text><text x="221" y="69">4.5</text>
        <text x="72" y="124">2.4</text><text x="121" y="122">2.5</text><text x="171" y="139">1.8</text><text x="221" y="113">2.8</text>
        <text x="72" y="161">1</text><text x="121" y="156">1.2</text><text x="171" y="119">2.6</text><text x="221" y="148">1.5</text>
      </g>
      <g font-size="7" font-weight="700" text-anchor="middle">
        <text x="72" y="176">0.4</text><text x="121" y="97">3.4</text><text x="171" y="68">4.5</text><text x="221" y="90">3.7</text>
      </g>
      <g font-size="5">
        <line x1="254" y1="150" x2="262" y2="150" stroke="var(--teal-dark)"/><text x="265" y="152">Series 1</text>
        <line x1="254" y1="158" x2="262" y2="158" stroke="var(--teal)"/><text x="265" y="160">Series 2</text>
        <line x1="254" y1="166" x2="262" y2="166" stroke="var(--lime)"/><text x="265" y="168">Series 3</text>
        <line x1="254" y1="174" x2="262" y2="174" stroke="var(--violet)"/><text x="265" y="176">Series 4</text>
      </g>
    </svg>
    <div class="brand brand-footer">LUMENVALE</div>
  </section>

  <section class="slide col-2 row-3">
    <div class="artwork-corner" role="img" aria-label="Small decorative green accent"></div>
    <h2 class="slide-heading">Table</h2>
    <table class="data-table">
      <thead>
        <tr><th>Title A</th><th>Title B</th><th>Title C</th><th>Title D</th><th>Title E</th></tr>
      </thead>
      <tbody>
        <tr><td>Text here</td><td>1234567890</td><td>1234567890</td><td>1234567890</td><td>1234567890</td></tr>
        <tr><td>Text here</td><td>1234567890</td><td>1234567890</td><td>1234567890</td><td>1234567890</td></tr>
        <tr><td>Text here</td><td>1234567890</td><td>1234567890</td><td>1234567890</td><td>1234567890</td></tr>
        <tr><td>Text here</td><td>1234567890</td><td>1234567890</td><td>1234567890</td><td>1234567890</td></tr>
        <tr><td>Text here</td><td>1234567890</td><td>1234567890</td><td>1234567890</td><td>1234567890</td></tr>
        <tr><td>Text here</td><td>1234567890</td><td>1234567890</td><td>1234567890</td><td>1234567890</td></tr>
        <tr><td>Text here</td><td>1234567890</td><td>1234567890</td><td>1234567890</td><td>1234567890</td></tr>
        <tr><td>Text here</td><td>1234567890</td><td>1234567890</td><td>1234567890</td><td>1234567890</td></tr>
      </tbody>
    </table>
    <div class="brand brand-footer">LUMENVALE</div>
  </section>

  <section class="slide col-3 row-3" style="left:830px;width:338px">
    <div class="artwork-band" style="width:338px;height:100px" role="img" aria-label="Decorative green artwork area"></div>
    <div class="brand brand-large" style="left:24px;top:116px"><span class="brand-dot"></span>LUMENVALE</div>
    <p class="cover-title" style="right:34px;top:180px;font-size:15px">Thank You</p>
    <p class="cover-date" style="right:34px;top:207px">November 3, 2013</p>
  </section>
</body>
</html>
```